Icons for Stopwatch / Timer App

We need a set of icons for a timer and stopwatch app called Vaplora! The icons need to be clear and simple and clearly demonstrate their function. The stopwatch and timer icons can be more complicated and may end up being used as the main icon / logo for the app.

The icons should be scalable to suit many different sizes.

There is no set colour scheme.

Set of icons required:

Stopwatch
Timer / Hourglass
Start
Stop
Pause
Lap
Reset
Mute
Audio / Alarm

```html
<!DOCTYPE html>
<html lang="en">
<head>
<meta charset="utf-8">
<title>Vaplora! – Control Button States</title>
<link rel="stylesheet" href="https://fonts.googleapis.com/css2?family=Comfortaa:wght@400&display=swap">
<style>
  :root {
    --canvas-bg: #e8e7df;
    --heading: #f3b300;
    --face: #e3e2d9;
  }
  html, body {
    margin: 0;
    padding: 0;
    overflow: hidden;
  }
  .canvas {
    position: relative;
    width: 1200px;
    height: 900px;
    background: var(--canvas-bg);
    overflow: hidden;
    font-family: "Comfortaa", sans-serif;
  }
  .state-title {
    position: absolute;
    left: 67px;
    margin: 0;
    font-weight: 400;
    font-size: 44px;
    line-height: 1;
    color: var(--heading);
    letter-spacing: 0.5px;
    white-space: nowrap;
  }
  .state-title--normal { top: 188px; }
  .state-title--pressed { top: 508px; }
  .button-row {
    position: absolute;
    left: 54px;
    display: flex;
    gap: 39.4px;
  }
  .button-row--normal { top: 292px; }
  .button-row--pressed { top: 603px; }
  .control-button {
    width: 120px;
    height: 120px;
    display: block;
  }
  .defs { position: absolute; width: 0; height: 0; }
</style>
</head>
<body>
<div class="canvas">
  <svg class="defs" aria-hidden="true">
    <defs>
      <linearGradient id="ringGradient" x1="0" y1="0" x2="0" y2="1">
        <stop offset="0" stop-color="#f2f1ea"/>
        <stop offset="1" stop-color="#d6d5cc"/>
      </linearGradient>
      <linearGradient id="rimGradient" x1="0" y1="0" x2="0" y2="1">
        <stop offset="0" stop-color="#cfcec3"/>
        <stop offset="1" stop-color="#9c9b8a"/>
      </linearGradient>
      <linearGradient id="iconGradient" x1="0" y1="0" x2="0" y2="1">
        <stop offset="0" stop-color="#f7d000"/>
        <stop offset="1" stop-color="#efae00"/>
      </linearGradient>
      <g id="buttonFace">
        <circle r="50" fill="url(#rimGradient)"/>
        <circle cy="-3" r="47" fill="#e3e2d9"/>
      </g>
      <g id="buttonBase">
        <circle r="56" fill="url(#ringGradient)" stroke="#d2d1c8" stroke-width="1.5"/>
        <use href="#buttonFace"/>
      </g>
      <g id="buttonBasePressed">
        <circle r="57" fill="#f4f3ec"/>
        <circle r="54.5" fill="url(#ringGradient)" stroke="#f7e000" stroke-width="4.5"/>
        <use href="#buttonFace"/>
      </g>
      <g id="iconPlay"><path fill="url(#iconGradient)" stroke="#c98f00" stroke-width="0.8" d="M-14 -18 L18 -3 L-14 12 Z"/></g>
      <g id="iconLap"><path fill="url(#iconGradient)" stroke="#c98f00" stroke-width="0.8" d="M-5 -17 H5 V-8 H14 V2 H5 V11 H-5 V2 H-14 V-8 H-5 Z"/></g>
      <g id="iconStop"><rect fill="url(#iconGradient)" stroke="#c98f00" stroke-width="0.8" x="-17" y="-20" width="34" height="34" rx="2"/></g>
      <g id="iconPause" fill="url(#iconGradient)" stroke="#c98f00" stroke-width="0.8">
        <rect x="-15" y="-20" width="12" height="34" rx="2"/>
        <rect x="3" y="-20" width="12" height="34" rx="2"/>
      </g>
      <g id="iconReset">
        <path fill="url(#iconGradient)" stroke="#c98f00" stroke-width="0.8" d="M9 -11 A13 13 0 1 0 12 2 L6 2 A7.5 7.5 0 1 1 5 -7 L1 -3 L14 -1 L13 -15 Z"/>
      </g>
      <g id="iconMute">
        <path fill="url(#iconGradient)" stroke="#c98f00" stroke-width="0.8" d="M-17 -9 H-10 L-1 -17 V11 L-10 3 H-17 Z"/>
        <path fill="none" stroke="#efb800" stroke-width="2.4" stroke-linecap="round" d="M4 -8 Q8 -3 4 2 M8 -12 Q15 -3 8 6 M-19 -15 L3 9"/>
      </g>
      <g id="iconAlarm" fill="url(#iconGradient)" stroke="#c98f00" stroke-width="0.8">
        <path d="M-1 -19 C-9 -19 -10 -10 -10 -3 C-10 4 -13 8 -17 11 H15 C11 8 8 4 8 -3 C8 -10 7 -19 -1 -19 Z"/>
        <circle cx="-1" cy="14" r="3.5"/>
      </g>
    </defs>
  </svg>

  <h2 class="state-title state-title--normal">Normal State</h2>
  <div class="button-row button-row--normal">
    <svg class="control-button" viewBox="-60 -60 120 120" role="img" aria-label="Start"><use href="#buttonBase"/><use href="#iconPlay"/></svg>
    <svg class="control-button" viewBox="-60 -60 120 120" role="img" aria-label="Lap"><use href="#buttonBase"/><use href="#iconLap"/></svg>
    <svg class="control-button" viewBox="-60 -60 120 120" role="img" aria-label="Stop"><use href="#buttonBase"/><use href="#iconStop"/></svg>
    <svg class="control-button" viewBox="-60 -60 120 120" role="img" aria-label="Pause"><use href="#buttonBase"/><use href="#iconPause"/></svg>
    <svg class="control-button" viewBox="-60 -60 120 120" role="img" aria-label="Reset"><use href="#buttonBase"/><use href="#iconReset"/></svg>
    <svg class="control-button" viewBox="-60 -60 120 120" role="img" aria-label="Mute"><use href="#buttonBase"/><use href="#iconMute"/></svg>
    <svg class="control-button" viewBox="-60 -60 120 120" role="img" aria-label="Alarm"><use href="#buttonBase"/><use href="#iconAlarm"/></svg>
  </div>

  <h2 class="state-title state-title--pressed">Pressed State</h2>
  <div class="button-row button-row--pressed">
    <svg class="control-button" viewBox="-60 -60 120 120" role="img" aria-label="Start pressed"><use href="#buttonBasePressed"/><use href="#iconPlay"/></svg>
    <svg class="control-button" viewBox="-60 -60 120 120" role="img" aria-label="Lap pressed"><use href="#buttonBasePressed"/><use href="#iconLap"/></svg>
    <svg class="control-button" viewBox="-60 -60 120 120" role="img" aria-label="Stop pressed"><use href="#buttonBasePressed"/><use href="#iconStop"/></svg>
    <svg class="control-button" viewBox="-60 -60 120 120" role="img" aria-label="Pause pressed"><use href="#buttonBasePressed"/><use href="#iconPause"/></svg>
    <svg class="control-button" viewBox="-60 -60 120 120" role="img" aria-label="Reset pressed"><use href="#buttonBasePressed"/><use href="#iconReset"/></svg>
    <svg class="control-button" viewBox="-60 -60 120 120" role="img" aria-label="Mute pressed"><use href="#buttonBasePressed"/><use href="#iconMute"/></svg>
    <svg class="control-button" viewBox="-60 -60 120 120" role="img" aria-label="Alarm pressed"><use href="#buttonBasePressed"/><use href="#iconAlarm"/></svg>
  </div>
</div>
</body>
</html>
```